Business Card: RW Office Partners - Your tidy answer finder

Business Name: RW Office Partners
Website: www.rwofficepartners.com.au
Email: marisol@rwofficepartners.com.au
Mobile: 61 487 902 346
Facebook: @rwofficepartners
Instrgram: @rwofficepartners

Brading Colours:
HEX
#986474
#ddccd3
#7a8498
#c9d8e4
#000000
#ffffff

Tag Line: Your organised problem solver

Link to DRAFT website:
https://helpdeskhub.sitebuilderx.com/rw-office-partners

About Page from the website:
My name is Marisol Bramwell, and I would love to assist you to become more productive in your day to day and achieve your business and personal goals.
My mission is to give you time, time to work on the important tasks of your business or to be able to spend more time with your family. I will take on the tasks you don’t have time for, don’t know well or simply don’t like to do.
I have an extensive background in Administration, Tender Coordination, Document Control, WHS and Quality Management working primarily in the Construction, Mining and Corporate World.
I am passionate about being organised, having order and making things in your life (and mine) easier! I love to watch something unfold and grow into something amazing! I am known for being the go-to problem solver, the organiser of all things, producing high standards of work even under pressure. I’m also a confident communicator, and I understand that you’re busy running your business.

Target Market(s)

Small to Medium Business who require assistance in their business by a virtual assistant.

Industry/Entity Type

Virtual Assistant

Contact Information for Business Card

Mobile: 61 487 902 346

Font styles to use
Sans Serif

Colors
ffffff

Requirements
Must have
• Branding Colours as outlined.
Contact Details as outlined.
Logo as provided.
Proper contact details - mobile, facebook, instragm, website.
Simple, Elegant, very clean looking.
Should not have
• Note cute with pictures.
Not too girly as still want to market to construction companies.

```html
<!DOCTYPE html>
<html lang="en">
<head>
<meta charset="utf-8">
<title>RW Office Partners – Business Card</title>
<link rel="stylesheet" href="https://fonts.googleapis.com/css2?family=Roboto:wght@400;500&display=swap">
<style>
  :root {
    --mauve: #986474;
    --mauve-soft: #ddccd3;
    --slate: #7a8498;
    --slate-soft: #c9d8e4;
    --ink: #3d3d44;
    --paper: #ffffff;
    --backdrop: #e9e9ec;
  }
  * { box-sizing: border-box; margin: 0; padding: 0; }
  html, body { width: 1200px; height: 900px; overflow: hidden; }
  body {
    background: var(--backdrop);
    font-family: "Roboto", Arial, sans-serif;
    position: relative;
  }
  .card {
    position: absolute;
    left: 267px;
    width: 665px;
    height: 380px;
    box-shadow: 0 6px 18px rgba(0,0,0,.18);
    overflow: hidden;
  }
  /* Back side */
  .card-back { top: 45px; background: var(--slate); }
  .card-back .texture {
    position: absolute; inset: 0;
    background: linear-gradient(135deg, #7f899d 0%, #76809 4 100%);
    background: linear-gradient(135deg, #818ba0 0%, #737d91 100%);
  }
  .card-back .back-name {
    position: absolute;
    right: 44px; top: 238px;
    color: var(--paper);
    font-weight: 500;
    font-size: 30px;
    letter-spacing: .5px;
  }
  /* Front side */
  .card-front { top: 475px; background: var(--paper); }
  .brand {
    position: absolute;
    left: 70px; top: 118px;
    width: 245px;
    color: var(--mauve);
    font-weight: 500;
    font-size: 38px;
    line-height: 1.08;
    text-transform: uppercase;
    letter-spacing: 1px;
  }
  .divider {
    position: absolute;
    left: 340px; top: 102px;
    width: 2px; height: 118px;
    background: var(--mauve);
  }
  .contacts {
    position: absolute;
    left: 362px; top: 104px;
    list-style: none;
    color: var(--ink);
    font-size: 17px;
  }
  .contacts li {
    display: flex; align-items: center;
    height: 28px;
  }
  .contacts svg { width: 14px; height: 14px; margin-right: 8px; flex: none; }
  .contacts .dot {
    width: 12px; height: 12px; border-radius: 50%;
    background: var(--mauve); margin-right: 9px; flex: none;
  }
  .footer-band { position: absolute; left: 0; bottom: 0; width: 665px; height: 60px; }
  .tagline {
    position: absolute;
    right: 26px; bottom: 20px;
    color: var(--paper);
    font-size: 17px;
  }
</style>
</head>
<body>
  <section class="card card-back">
    <div class="texture" role="img" aria-label="Faint repeating brand monogram pattern on slate background"></div>
    <span class="back-name">RW Office Partners</span>
  </section>

  <section class="card card-front">
    <div class="brand">RW Office Partners</div>
    <div class="divider"></div>
    <ul class="contacts">
      <li>
        <svg viewBox="0 0 24 24" aria-hidden="true"><path fill="#986474" d="M6.6 10.8c1.4 2.8 3.8 5.1 6.6 6.6l2.2-2.2c.3-.3.7-.4 1-.2 1.1.4 2.3.6 3.6.6.6 0 1 .4 1 1V20c0 .6-.4 1-1 1C10.6 21 3 13.4 3 4c0-.6.4-1 1-1h3.5c.6 0 1 .4 1 1 0 1.3.2 2.5.6 3.6.1.3 0 .7-.2 1z"/></svg>
        61 487 902 346
      </li>
      <li>
        <svg viewBox="0 0 24 24" aria-hidden="true"><path fill="#986474" d="M2 5h20v14H2z"/><path fill="none" stroke="#fff" stroke-width="2" d="M2 5l10 8 10-8"/></svg>
        marisol@rwofficepartners.com.au
      </li>
      <li>
        <svg viewBox="0 0 24 24" aria-hidden="true"><circle cx="12" cy="12" r="10" fill="#986474"/><path fill="none" stroke="#fff" stroke-width="1.5" d="M2 12h20M12 2c3 3 3 17 0 20M12 2c-3 3-3 17 0 20"/></svg>
        www.rwofficepartners.com.au
      </li>
      <li>
        <span class="dot"></span>
        @rwofficepartners
      </li>
    </ul>

    <svg class="footer-band" viewBox="0 0 665 60" aria-hidden="true">
      <polygon points="0,60 0,52 395,52 395,60" fill="#986474"/>
      <polygon points="388,60 395,20 665,20 665,60" fill="#7a8498"/>
      <polygon points="0,52 395,40 395,52" fill="#986474"/>
    </svg>
    <span class="tagline">Your tidy answer finder</span>
  </section>
</body>
</html>
```